Corporate Branding - Web and Print

A UK based company will like to use an existing logo to create branding materials for all marketing related documents, including business card, prints, letterhead, Website, Twitter, Facebook, Instagram logo etc. This company serves high-end clientele in the fashion, health and wellness and as such high quality and class is of utmost importance.
Where the logo can be modernised without losing its character then experiment. The main thing is to have a corporate branding which can be used later for brochures, Business Plan infographics.
The prominent colour within the organisation is burnt orange with no secondary colour. However if you believe a secondary colour is needed then use it, otherwise keep it simple and classy. Any chosen colours have to match perfectly.
Target Market(s)
High net worth individuals
Industry/Entity Type
Health And Wellness
Contact Information for Business Card
classy
Look and feel
Each slider illustrates characteristics of the customer's brand and the style your logo design should communicate.

```html
<!DOCTYPE html>
<html lang="en">
<head>
<meta charset="utf-8">
<title>Velora — Business Card</title>
<link rel="stylesheet" href="https://fonts.googleapis.com/css2?family=Arimo:wght@400;700&display=swap">
<style>
  :root {
    --page-bg: #161616;
    --card-dark: #2a2a2b;
    --card-mid: #3a3a3c;
    --burnt-orange: #e8762a;
    --accent-orange: #f07d3c;
  }
  * { box-sizing: border-box; margin: 0; padding: 0; }
  html, body {
    width: 956px;
    height: 1200px;
    overflow: hidden;
    background: var(--page-bg);
    font-family: "Arimo", Arial, sans-serif;
  }
  .canvas { position: relative; width: 956px; height: 1200px; }

  .card {
    position: absolute;
    background: linear-gradient(180deg, var(--card-mid) 0%, var(--card-dark) 55%, var(--card-mid) 100%);
  }
  .card--front { left: 103px; top: 115px; width: 761px; height: 428px; }
  .card--back  { left: 108px; top: 638px; width: 756px; height: 426px; }

  .front-brand {
    position: absolute;
    left: 0; right: 0; top: 0; bottom: 0;
    display: flex; align-items: center; justify-content: center;
    color: var(--burnt-orange);
    font-weight: 700;
    font-size: 60px;
    letter-spacing: 4px;
  }

  .back-brand {
    position: absolute;
    left: 52px; top: 45px;
    display: flex; align-items: center; gap: 24px;
  }
  .back-brand__dot {
    width: 70px; height: 70px; border-radius: 50%;
    background: var(--burnt-orange);
  }
  .back-brand__name {
    color: var(--burnt-orange);
    font-weight: 700;
    font-size: 46px;
    letter-spacing: 3px;
  }

  .contact-list { position: absolute; left: 60px; top: 198px; list-style: none; }
  .contact-item {
    display: flex; align-items: center;
    height: 36px; margin-bottom: 30px;
    color: var(--accent-orange);
    font-size: 23px;
  }
  .contact-item:nth-child(3) { margin-top: 4px; }
  .contact-icon { width: 38px; height: 38px; margin-right: 28px; flex: none; }

  .divider {
    position: absolute; left: 496px; top: 180px;
    width: 2px; height: 202px;
    background: var(--burnt-orange);
  }

  .social-list { position: absolute; left: 514px; top: 198px; list-style: none; }
  .social-item { width: 38px; height: 38px; margin-bottom: 26px; }
  .social-item:nth-child(3) { margin-top: 6px; }
  .social-square { width: 30px; height: 30px; margin: 4px; background: var(--accent-orange); }
  .social-circle { width: 32px; height: 32px; margin: 3px; border-radius: 50%; background: var(--accent-orange); }
</style>
</head>
<body>
<main class="canvas">

  <section class="card card--front" aria-label="Business card front">
    <div class="front-brand">VELORA</div>
  </section>

  <section class="card card--back" aria-label="Business card back">
    <div class="back-brand">
      <span class="back-brand__dot"></span>
      <span class="back-brand__name">VELORA</span>
    </div>

    <ul class="contact-list">
      <li class="contact-item">
        <svg class="contact-icon" viewBox="0 0 38 38" aria-hidden="true">
          <circle cx="19" cy="19" r="17" fill="var(--accent-orange)"/>
          <path d="M13 10c1.5-1 2.5-.5 3.2 1l1.3 3c.4 1-.2 1.8-1.2 2.4 1 2.3 2.6 4.1 4.8 5.2.6-1 1.4-1.6 2.4-1.2l3 1.3c1.4.7 1.9 1.7.9 3.2-1.2 1.8-3.2 2.4-5.2 1.6-4.6-1.9-8-5.3-9.9-9.9-.8-2-.2-4 .7-4.6z" fill="#fff"/>
        </svg>
        +44770090418
      </li>
      <li class="contact-item">
        <svg class="contact-icon" viewBox="0 0 38 38" aria-hidden="true">
          <rect x="1" y="8" width="36" height="23" fill="var(--accent-orange)"/>
          <path d="M1 8l18 14L37 8" fill="none" stroke="#2c2c2d" stroke-width="2"/>
        </svg>
        hello@velora.uk
      </li>
      <li class="contact-item">
        <svg class="contact-icon" viewBox="0 0 38 38" aria-hidden="true">
          <path d="M19 2c-7 0-12 5-12 12 0 8 12 22 12 22s12-14 12-22c0-7-5-12-12-12z" fill="var(--accent-orange)"/>
          <circle cx="19" cy="14" r="5" fill="#2c2c2d"/>
        </svg>
        12 Marlow Lane, Bristol, UK
      </li>
    </ul>

    <div class="divider"></div>

    <ul class="social-list">
      <li class="social-item" aria-label="Website">
        <svg viewBox="0 0 38 38" width="38" height="38" aria-hidden="true">
          <g fill="none" stroke="var(--accent-orange)" stroke-width="2.2">
            <circle cx="19" cy="19" r="16"/>
            <ellipse cx="19" cy="19" rx="7" ry="16"/>
            <line x1="19" y1="3" x2="19" y2="35"/>
            <line x1="3" y1="19" x2="35" y2="19"/>
            <path d="M6 11h26M6 27h26"/>
          </g>
        </svg>
      </li>
      <li class="social-item" aria-label="Social profile"><div class="social-square"></div></li>
      <li class="social-item" aria-label="Social profile"><div class="social-circle"></div></li>
    </ul>
  </section>

</main>
</body>
</html>
```